Peanut Butter for Dogs - Label

Dear Designers,

Our company develops natural & innovative products aimed at enhancing animal (cat & dog) well-being. The company focuses on producing high-end, ethically sourced products that naturally soothe pets, improving their quality of life.

We are currently developing a new CBD-enriched Peanut Butter product for dogs, and we are looking for some label designs that follow our brand image & brand identity.

-> Please see full brief PDF file attached.

Target Market(s)

European Market (French Speaking)

Industry/Entity Type

Pet Food

Font styles to use
Other font styles liked:
• Please see brand kit in PDF brief

Colors

Designer to choose colors to be used in the design.

Requirements
Must have
• Please see brief PDF file attached
Nice to have
Should not have

```html
<!DOCTYPE html>
<html lang="fr">
<head>
<meta charset="utf-8">
<title>Verdalia – Douceur Réconfortante – Étiquette</title>
<link rel="stylesheet" href="https://fonts.googleapis.com/css2?family=Montserrat:wght@300;400;500;600&display=swap">
<style>
  :root {
    --teal: #3a9a7e;
    --teal-light: #e4f2ed;
    --ink: #2b2b2b;
    --grey-text: #444;
    --orange: #e8922e;
    --paper: #ffffff;
    --page: #ffffff;
  }
  * { box-sizing: border-box; margin: 0; padding: 0; }
  html, body {
    width: 975px; height: 1200px; overflow: hidden;
    background: var(--page);
    font-family: "Montserrat", sans-serif;
    color: var(--grey-text);
  }
  .canvas { position: relative; width: 975px; height: 1200px; }

  .label {
    position: absolute; left: 37px; width: 900px; height: 225px;
    background: var(--paper); overflow: hidden;
  }
  .label--first { top: 343px; }
  .label--second { top: 631px; }

  .label__frame { position: absolute; inset: 0; width: 900px; height: 225px; }

  .intro {
    position: absolute; left: 21px; top: 28px; width: 254px;
    font-size: 10px; line-height: 14.6px; font-weight: 300;
    text-align: justify; color: var(--ink);
  }
  .intro strong { font-weight: 600; }
  .section-title {
    font-size: 15px; font-weight: 400; color: var(--teal);
    letter-spacing: 0.2px; margin: 10px 0 1px;
  }

  .brand {
    position: absolute; left: 330px; top: 24px; width: 86px;
    display: flex; flex-direction: column; align-items: center; gap: 4px;
  }
  .brand__dot { width: 12px; height: 12px; border-radius: 50%; background: var(--teal); }
  .brand__name { font-size: 11px; font-weight: 500; color: var(--ink); letter-spacing: 0.5px; }

  .badges { position: absolute; left: 447px; top: 22px; display: flex; gap: 6px; }
  .badge {
    width: 36px; height: 36px; border-radius: 50%;
    border: 1.5px solid var(--teal); display: flex; align-items: center; justify-content: center;
  }
  .badge span { width: 20px; height: 20px; border-radius: 50%; background: var(--teal); opacity: 0.85; }

  .product-name {
    position: absolute; left: 316px; top: 66px;
    font-size: 15px; line-height: 17px; font-weight: 600; letter-spacing: 0.2px;
  }
  .product-name .accent { color: var(--teal); display: block; }
  .product-name .main { color: var(--ink); display: block; }
  .product-name .rule { display: block; width: 107px; height: 1.5px; background: var(--teal); margin-top: 3px; }
  .dose-tag { display: block; font-size: 9.5px; font-weight: 500; color: var(--ink); margin: 3px 0 0 3px; }
  .dose-tag b { color: var(--teal); font-weight: 500; }

  .flavour {
    position: absolute; left: 326px; top: 137px; width: 56px; height: 56px;
    border-radius: 50%; background: var(--orange);
    display: flex; align-items: center; justify-content: center;
  }
  .flavour__inner {
    width: 48px; height: 48px; border-radius: 50%;
    border: 1px dashed rgba(255,255,255,0.8);
    display: flex; flex-direction: column; align-items: center; justify-content: center;
    color: #fff; font-size: 5.6px; line-height: 7px; text-align: center; font-weight: 400;
  }
  .flavour__inner b { font-weight: 600; }

  .nuts {
    position: absolute; left: 391px; top: 140px; width: 86px; height: 62px;
    border-radius: 45% 40% 30% 35%;
    background: radial-gradient(ellipse at 45% 45%, #c58a55 0%, #a8693a 60%, rgba(168,105,58,0) 100%);
  }

  .photo {
    position: absolute; left: 474px; top: 69px; width: 156px; height: 156px;
    border-radius: 50%; border: 9px solid var(--teal);
    background: linear-gradient(160deg, #ececec 0%, #d9d9d9 55%, #c8c8c8 100%);
  }

  .ingredients {
    position: absolute; left: 645px; top: 16px; width: 233px; height: 29px;
    border: 1px dashed var(--teal); border-radius: 5px;
    font-size: 6.6px; color: var(--ink); text-align: center; padding-top: 12px; font-weight: 400;
  }
  .ingredients__title {
    position: absolute; left: 50%; top: -7px; transform: translateX(-50%);
    background: var(--paper); padding: 0 6px;
    font-size: 11.5px; color: var(--teal); font-weight: 400; letter-spacing: 0.3px; white-space: nowrap;
  }

  .dosage {
    position: absolute; left: 684px; top: 52px; width: 156px;
    border-collapse: collapse; font-size: 8px; font-weight: 300;
  }
  .dosage th {
    background: var(--teal); color: #fff; font-weight: 400; height: 14px; font-size: 8px;
  }
  .dosage td { height: 15.5px; border: 1px solid #b9ddd0; color: var(--ink); text-align: center; }
  .dosage td.size { background: var(--teal); color: #d8efe6; text-align: right; padding-right: 5px; width: 64px; border-color: #fff; }
  .dosage td.size::before {
    content: ""; display: inline-block; width: 9px; height: 5px; background: #fff;
    border-radius: 2px; margin-right: 3px; vertical-align: middle;
  }

  .tip { position: absolute; left: 643px; top: 124px; width: 237px; font-size: 10px; line-height: 14.6px; font-weight: 300; color: var(--ink); text-align: justify; }
  .tip .section-title { margin: 0 0 1px; }
  .tip strong { font-weight: 600; }

  .net-weight {
    position: absolute; left: 737px; top: 187px; right: 0;
    display: flex; align-items: center; gap: 4px; font-size: 10px;
  }
  .net-weight .lbl { color: var(--teal); font-weight: 300; }
  .net-weight .val { color: var(--ink); font-weight: 500; }
  .net-weight .line { flex: 1; height: 1.5px; background: var(--teal); margin-left: 2px; }
</style>
</head>
<body>
<main class="canvas">

  <section class="label label--first">
    <svg class="label__frame" viewBox="0 0 900 225" aria-hidden="true">
      <path d="M0 1 H362 Q370 1 373 12 Q376 1 384 1 H900 V5 H386 Q378 5 373 18 Q368 5 360 5 H0 Z" fill="#3a9a7e"/>
      <rect x="0" y="206" width="900" height="19" fill="#3a9a7e"/>
    </svg>

    <div class="intro">
      <p>Doux comme une caresse Enrichi en extrait de chanvre naturellement apaisant, le beurre de cacahuète <strong>VERDANUTS™</strong> est une délicieuse friandise d’occupation à lécher.</p>
      <h3 class="section-title">UTILISATION</h3>
      <p>Laissez votre chien lécher cette gourmandise pour traverser en douceur les événements stressants du quotidien (absence, toilettage, trajet en voiture, etc.)</p>
    </div>

    <div class="brand"><span class="brand__dot"></span><span class="brand__name">VERDALIA</span></div>

    <div class="badges">
      <div class="badge" title="Anti-stress"><span></span></div>
      <div class="badge" title="100% naturel"><span></span></div>
      <div class="badge" title="À lécher"><span></span></div>
    </div>

    <h2 class="product-name">
      <span class="accent">DOUCEUR</span>
      <span class="main">RÉCONFORTANTE</span>
      <span class="rule"></span>
      <span class="dose-tag"><b>CBD</b> 150MG</span>
      <span class="rule"></span>
    </h2>

    <div class="flavour"><div class="flavour__inner">BEURRE DE<b>CACAHUÈTE</b></div></div>
    <div class="nuts" role="img" aria-label="Photo d’un tas d’amandes"></div>
    <div class="photo" role="img" aria-label="Photo d’un chien shar-pei blanc tirant la langue"></div>

    <div class="ingredients">
      <span class="ingredients__title">INGRÉDIENTS</span>
      Beurre de cacahuète, extrait de chanvre (0% THC).
    </div>

    <table class="dosage">
      <tr><th>TAILLE</th><th>DOSAGE</th></tr>
      <tr><td class="size">Petit</td><td>1 cuillère à café</td></tr>
      <tr><td class="size">Moyen</td><td>2 cuillères à café</td></tr>
      <tr><td class="size">Grand</td><td>3 cuillères à café</td></tr>
    </table>

    <div class="tip">
      <h3 class="section-title">ASTUCE</h3>
      <p>Pour une utilisation optimale, étalez le beurre de cacahuète sur le tapis de léchage <strong>VERDALICK™</strong>.</p>
    </div>

    <div class="net-weight"><span class="lbl">Poids Net :</span><span class="val">250g</span><span class="line"></span></div>
  </section>

  <section class="label label--second">
    <svg class="label__frame" viewBox="0 0 900 225" aria-hidden="true">
      <path d="M0 1 H362 Q370 1 373 12 Q376 1 384 1 H900 V5 H386 Q378 5 373 18 Q368 5 360 5 H0 Z" fill="#3a9a7e"/>
      <rect x="0" y="206" width="900" height="19" fill="#3a9a7e"/>
    </svg>

    <div class="intro">
      <p>Doux comme une caresse Enrichi en extrait de chanvre naturellement apaisant, le beurre de cacahuète <strong>VERDANUTS™</strong> est une délicieuse friandise d’occupation à lécher.</p>
      <h3 class="section-title">UTILISATION</h3>
      <p>Laissez votre chien lécher cette gourmandise pour traverser en douceur les événements stressants du quotidien (absence, toilettage, trajet en voiture, etc.)</p>
    </div>

    <div class="brand"><span class="brand__dot"></span><span class="brand__name">VERDALIA</span></div>

    <div class="badges">
      <div class="badge" title="Anti-stress"><span></span></div>
      <div class="badge" title="100% naturel"><span></span></div>
      <div class="badge" title="À lécher"><span></span></div>
    </div>

    <h2 class="product-name">
      <span class="accent">DOUCEUR</span>
      <span class="main">RÉCONFORTANTE</span>
      <span class="rule"></span>
      <span class="dose-tag"><b>CBD</b> 150MG</span>
      <span class="rule"></span>
    </h2>

    <div class="flavour"><div class="flavour__inner">BEURRE DE<b>CACAHUÈTE</b></div></div>
    <div class="nuts" role="img" aria-label="Photo d’un tas d’amandes"></div>
    <div class="photo" role="img" aria-label="Photo d’un chien shar-pei blanc tirant la langue"></div>

    <div class="ingredients">
      <span class="ingredients__title">INGRÉDIENTS</span>
      Beurre de cacahuète, extrait de chanvre (0% THC).
    </div>

    <table class="dosage">
      <tr><th>TAILLE</th><th>DOSAGE</th></tr>
      <tr><td class="size">Petit</td><td>1 cuillère à café</td></tr>
      <tr><td class="size">Moyen</td><td>2 cuillères à café</td></tr>
      <tr><td class="size">Grand</td><td>3 cuillères à café</td></tr>
    </table>

    <div class="tip">
      <h3 class="section-title">ASTUCE</h3>
      <p>Pour une utilisation optimale, étalez le beurre de cacahuète sur le tapis de léchage <strong>VERDALICK™</strong>.</p>
    </div>

    <div class="net-weight"><span class="lbl">Poids Net :</span><span class="val">250g</span><span class="line"></span></div>
  </section>

</main>
</body>
</html>
```